Business Card Design Project

Company name will be Tallow Crest (named after my black lab and his fraying muzzle) Business is in the body armor, Security product industry servicing the state, local, and federal law enforcement markets. I want a more formal and serious logo for both business cards and letterhead

```html
<!DOCTYPE html>
<html lang="en">
<head>
<meta charset="utf-8">
<title>Tallow Crest — Business Cards</title>
<link rel="stylesheet" href="https://fonts.googleapis.com/css2?family=Questrial&display=swap">
<style>
  :root {
    --page-bg: #e4e0da;
    --charcoal: #333333;
    --charcoal-text: #e2e2e2;
    --charcoal-sub: #b4b4b4;
    --silver-light: #f2f2ee;
    --silver-dark: #c9c6bc;
    --silver-text: #3c3c3c;
    --silver-sub: #4a4a4a;
    --maroon: #6c1410;
    --maroon-text: #ececec;
    --maroon-sub: #d6d0d0;
    --chip-light: #ffffff;
    --chip-dark: #3e3e3e;
    --ink: #222222;
  }
  * { box-sizing: border-box; margin: 0; padding: 0; }
  html, body { width: 1200px; height: 1000px; overflow: hidden; }
  body {
    background: var(--page-bg);
    font-family: "Questrial", "Helvetica Neue", Arial, sans-serif;
    position: relative;
  }
  .card {
    position: absolute;
    width: 531px;
    height: 323px;
    transform-origin: top left;
    overflow: hidden;
  }
  .card--charcoal { left: 347px; top: 67px; background: var(--charcoal); color: var(--charcoal-text); }
  .card--silver {
    left: 138px; top: 665px; transform: scale(0.759);
    background: linear-gradient(100deg, var(--silver-light) 0%, #dcdad3 45%, var(--silver-dark) 100%);
    color: var(--silver-text);
  }
  .card--maroon { left: 677px; top: 667px; transform: scale(0.752); background: var(--maroon); color: var(--maroon-text); }

  .brand-mark {
    position: absolute;
    left: 38px; top: 46px;
    width: 40px; height: 40px;
    background: currentColor;
    opacity: 0.85;
  }
  .brand-name {
    position: absolute;
    left: 180px; top: 48px;
    font-size: 48px;
    letter-spacing: 0.5px;
    white-space: nowrap;
  }
  .tagline {
    position: absolute;
    left: 145px; top: 136px;
    font-size: 17px;
    white-space: nowrap;
  }
  .card--charcoal .tagline { color: var(--charcoal-sub); }
  .card--silver .tagline { color: var(--silver-sub); }
  .card--maroon .tagline { color: var(--maroon-sub); }

  .chip {
    position: absolute;
    display: flex;
    align-items: center;
    gap: 5px;
    background: var(--chip-light);
    color: var(--ink);
    white-space: nowrap;
  }
  .chip svg { display: block; flex: none; }
  .chip--email { right: 0; top: 257px; height: 21px; padding: 0 8px 0 4px; font-size: 10.5px; }
  .chip--phone { right: 0; top: 293px; height: 24px; padding: 0 6px 0 4px; font-size: 14px; }
  .chip--address { left: 0; top: 297px; height: 21px; padding: 0 6px 0 4px; font-size: 10.5px; }
  .card--silver .chip--email,
  .card--silver .chip--address { background: var(--chip-dark); color: #ffffff; }
</style>
</head>
<body>

  <section class="card card--charcoal" aria-label="Business card, charcoal">
    <span class="brand-mark" aria-hidden="true"></span>
    <h1 class="brand-name">Tallow Crest</h1>
    <p class="tagline">Ray Holden&nbsp; Manufacturers Rep Principal</p>
    <div class="chip chip--email">
      <svg width="26" height="14" viewBox="0 0 26 14"><rect x="0.5" y="0.5" width="25" height="13" fill="none" stroke="#666"/><path d="M0.5 0.5 L13 8 L25.5 0.5" fill="none" stroke="#666"/></svg>
      rholdenpe1@mailbox.com
    </div>
    <div class="chip chip--address">
      1480 Harbor Lane East, Port Ellery, FL 32011
      <svg width="24" height="20" viewBox="0 0 24 20"><path d="M12 1 L23 10 L20 10 L20 19 L4 19 L4 10 L1 10 Z" fill="#444"/><rect x="10" y="13" width="4" height="6" fill="#fff"/></svg>
    </div>
    <div class="chip chip--phone">
      <svg width="14" height="20" viewBox="0 0 14 20"><rect x="0.5" y="0.5" width="13" height="19" rx="1.5" fill="#444"/><rect x="2.5" y="2.5" width="9" height="6" fill="#fff"/><g fill="#fff"><rect x="2.5" y="11" width="2" height="2"/><rect x="6" y="11" width="2" height="2"/><rect x="9.5" y="11" width="2" height="2"/><rect x="2.5" y="14.5" width="2" height="2"/><rect x="6" y="14.5" width="2" height="2"/><rect x="9.5" y="14.5" width="2" height="2"/></g></svg>
      555-310-4426
    </div>
  </section>

  <section class="card card--silver" aria-label="Business card, silver">
    <span class="brand-mark" aria-hidden="true"></span>
    <h2 class="brand-name">Tallow Crest</h2>
    <p class="tagline">Ray Holden&nbsp; Manufacturers Rep Principal</p>
    <div class="chip chip--email">
      <svg width="26" height="14" viewBox="0 0 26 14"><rect x="0.5" y="0.5" width="25" height="13" fill="none" stroke="#bbb"/><path d="M0.5 0.5 L13 8 L25.5 0.5" fill="none" stroke="#bbb"/></svg>
      rholdenpe1@mailbox.com
    </div>
    <div class="chip chip--address">
      1480 Harbor Lane East, Port Ellery, FL 32011
      <svg width="24" height="20" viewBox="0 0 24 20"><path d="M12 1 L23 10 L20 10 L20 19 L4 19 L4 10 L1 10 Z" fill="#666"/><rect x="10" y="13" width="4" height="6" fill="#3e3e3e"/></svg>
    </div>
    <div class="chip chip--phone">
      <svg width="14" height="20" viewBox="0 0 14 20"><rect x="0.5" y="0.5" width="13" height="19" rx="1.5" fill="#444"/><rect x="2.5" y="2.5" width="9" height="6" fill="#fff"/><g fill="#fff"><rect x="2.5" y="11" width="2" height="2"/><rect x="6" y="11" width="2" height="2"/><rect x="9.5" y="11" width="2" height="2"/><rect x="2.5" y="14.5" width="2" height="2"/><rect x="6" y="14.5" width="2" height="2"/><rect x="9.5" y="14.5" width="2" height="2"/></g></svg>
      555-310-4426
    </div>
  </section>

  <section class="card card--maroon" aria-label="Business card, maroon">
    <span class="brand-mark" aria-hidden="true"></span>
    <h2 class="brand-name">Tallow Crest</h2>
    <p class="tagline">Ray Holden&nbsp; Manufacturers Rep Principal</p>
    <div class="chip chip--email">
      <svg width="26" height="14" viewBox="0 0 26 14"><rect x="0.5" y="0.5" width="25" height="13" fill="none" stroke="#666"/><path d="M0.5 0.5 L13 8 L25.5 0.5" fill="none" stroke="#666"/></svg>
      rholdenpe1@mailbox.com
    </div>
    <div class="chip chip--address">
      1480 Harbor Lane East, Port Ellery, FL 32011
      <svg width="24" height="20" viewBox="0 0 24 20"><path d="M12 1 L23 10 L20 10 L20 19 L4 19 L4 10 L1 10 Z" fill="#444"/><rect x="10" y="13" width="4" height="6" fill="#fff"/></svg>
    </div>
    <div class="chip chip--phone">
      <svg width="14" height="20" viewBox="0 0 14 20"><rect x="0.5" y="0.5" width="13" height="19" rx="1.5" fill="#444"/><rect x="2.5" y="2.5" width="9" height="6" fill="#fff"/><g fill="#fff"><rect x="2.5" y="11" width="2" height="2"/><rect x="6" y="11" width="2" height="2"/><rect x="9.5" y="11" width="2" height="2"/><rect x="2.5" y="14.5" width="2" height="2"/><rect x="6" y="14.5" width="2" height="2"/><rect x="9.5" y="14.5" width="2" height="2"/></g></svg>
      555-310-4426
    </div>
  </section>

</body>
</html>
```